KORVANTIX Banner

We are looking to make an ~82" x 32" stand up vertical banner that includes our company’s service. This banner will be used at trade shows and should emphasize that we are a Managed Intelligence Provider. We basically want to try and turn the attached ad we are currently running, into a banner format. I've also attached two versions of our logo.

```html
<!DOCTYPE html>
<html lang="en">
<head>
<meta charset="utf-8">
<title>KORVANTIX Banner</title>
<link rel="stylesheet" href="https://fonts.googleapis.com/css2?family=Archivo+Black&family=Montserrat:wght@300;400;700;800;900&display=swap">
<style>
  :root {
    --navy: #041033;
    --blue-deep: #1872bb;
    --blue-soft: #65a3d8;
    --blue-title: #1a75c0;
    --paper: #ececec;
    --paper-light: #f4f4f4;
    --white: #ffffff;
  }
  * { box-sizing: border-box; margin: 0; padding: 0; }
  html, body { width: 1200px; height: 2680px; overflow: hidden; background: var(--white); }
  .banner {
    position: absolute; left: 79px; top: 4px;
    width: 1042px; height: 2672px;
    background: var(--paper);
    overflow: hidden;
  }
  .hero {
    position: absolute; left: 0; top: 0; width: 100%; height: 749px;
    background: linear-gradient(180deg, var(--paper-light), var(--paper));
    text-align: center;
  }
  .hero-kicker {
    position: absolute; left: 0; right: 0; top: 58px;
    font: 400 66px/1 "Montserrat", sans-serif; letter-spacing: -2px; color: var(--navy);
  }
  .hero-title {
    position: absolute; left: 0; right: 0; top: 158px;
    font: 800 92px/1 "Montserrat", sans-serif; letter-spacing: -4px; color: var(--blue-title);
  }
  .hero-illustration {
    position: absolute; left: 258px; top: 290px; width: 528px; height: 290px;
    border-radius: 264px 264px 20px 20px;
    background: radial-gradient(ellipse at 50% 100%, rgba(26,117,192,0.18), rgba(26,117,192,0.04) 70%, transparent);
  }
  .hero-heading {
    position: absolute; left: 0; right: 0; top: 622px;
    font: 900 86px/1 "Montserrat", sans-serif; letter-spacing: 1px; color: var(--navy);
  }
  .pillars { position: absolute; left: 8px; top: 749px; width: 116px; height: 1473px; }
  .pillar {
    position: absolute; left: 0; width: 116px;
    writing-mode: vertical-rl;
    display: flex; align-items: center; justify-content: center;
    font: 400 46px/50px "Archivo Black", sans-serif; color: var(--white); text-align: center;
  }
  .pillar--navy { background: var(--navy); }
  .pillar--blue { background: var(--blue-deep); }
  .pillar-know { top: 0; height: 435px; }
  .pillar-comm { top: 444px; height: 545px; }
  .pillar-commit { top: 1001px; height: 472px; }
  .services { position: absolute; left: 133px; top: 749px; width: 909px; height: 1473px; }
  .service {
    position: absolute; left: 0; width: 909px; height: 246px;
    background: var(--blue-soft);
    box-shadow: inset 0 10px 12px -8px rgba(4,16,51,0.35);
  }
  .service-icon-cell {
    position: absolute; left: 0; top: 0; width: 231px; height: 100%;
    background: var(--blue-deep);
  }
  .service-icon-cell::after {
    content: ""; position: absolute; right: -28px; top: 50%; margin-top: -28px;
    border-left: 28px solid var(--blue-deep); border-top: 28px solid transparent; border-bottom: 28px solid transparent;
  }
  .service-icon {
    position: absolute; left: 56px; top: 63px; width: 120px; height: 120px;
    border-radius: 24px; background: rgba(255,255,255,0.16);
  }
  .service-name {
    position: absolute; left: 303px; top: 50%; transform: translateY(-50%);
    font: 400 49px/66px "Archivo Black", sans-serif; color: var(--white); letter-spacing: 1px;
  }
  .footer {
    position: absolute; left: 0; top: 2232px; width: 100%; height: 440px;
    background: var(--navy); color: var(--white);
  }
  .brand { position: absolute; left: 0; right: 0; top: 72px; display: flex; justify-content: center; align-items: center; gap: 22px; }
  .brand-dot { width: 84px; height: 84px; border-radius: 50%; background: var(--blue-deep); }
  .brand-name { font: 700 46px/1 "Montserrat", sans-serif; letter-spacing: 1px; }
  .brand-tagline { font: 400 20px/1 "Montserrat", sans-serif; letter-spacing: 7px; margin-top: 10px; }
  .contacts {
    position: absolute; left: 0; right: 0; top: 228px;
    display: flex; justify-content: center; align-items: center; gap: 30px;
    font: 400 30px/1 "Archivo Black", sans-serif; letter-spacing: 2px;
  }
  .contact { display: flex; align-items: center; gap: 14px; }
  .contact-badge { width: 40px; height: 40px; border-radius: 50%; background: var(--blue-deep); display: flex; align-items: center; justify-content: center; }
  .contact-divider { width: 3px; height: 50px; background: var(--white); }
  .website {
    position: absolute; left: 0; right: 0; top: 324px;
    display: flex; justify-content: center; align-items: center; gap: 0;
    font: 400 45px/1 "Archivo Black", sans-serif; letter-spacing: 1px;
  }
  .website-badge { width: 106px; height: 106px; border-radius: 50%; background: var(--blue-deep); display: flex; align-items: center; justify-content: center; margin-right: -8px; }
</style>
</head>
<body>
<main class="banner">
  <header class="hero">
    <p class="hero-kicker">Lay a Stronger Foundation with</p>
    <h1 class="hero-title">The Best Technology!</h1>
    <div class="hero-illustration" role="img" aria-label="Circuit arcs over a cluster of gears with a check mark, representing automation"></div>
    <h2 class="hero-heading">AUTOMATION</h2>
  </header>

  <aside class="pillars">
    <div class="pillar pillar--navy pillar-know">MORE<br>KNOW-HOW</div>
    <div class="pillar pillar--blue pillar-comm">MORE<br>COMMUNICATION</div>
    <div class="pillar pillar--navy pillar-commit">MORE<br>COMMITMENT</div>
  </aside>

  <section class="services">
    <article class="service" style="top:0">
      <div class="service-icon-cell"><div class="service-icon" role="img" aria-label="Head with gear and brain icon"></div></div>
      <h3 class="service-name">ARTIFICIAL<br>INTELLIGENCE</h3>
    </article>
    <article class="service" style="top:245px">
      <div class="service-icon-cell"><div class="service-icon" role="img" aria-label="Circuit chip with chess knight icon"></div></div>
      <h3 class="service-name">TECHNOLOGY<br>STRATEGY</h3>
    </article>
    <article class="service" style="top:490px">
      <div class="service-icon-cell"><div class="service-icon" role="img" aria-label="Shield with keyhole icon"></div></div>
      <h3 class="service-name">MANAGED<br>CYBERSECURITY</h3>
    </article>
    <article class="service" style="top:736px">
      <div class="service-icon-cell"><div class="service-icon" role="img" aria-label="Hand holding gears icon"></div></div>
      <h3 class="service-name">MANAGED<br>IT SERVICES</h3>
    </article>
    <article class="service" style="top:981px">
      <div class="service-icon-cell"><div class="service-icon" role="img" aria-label="Support technician at laptop within gear icon"></div></div>
      <h3 class="service-name">CO-MANAGED<br>IT SERVICES</h3>
    </article>
    <article class="service" style="top:1227px">
      <div class="service-icon-cell"><div class="service-icon" role="img" aria-label="Phone handset with speaker icon"></div></div>
      <h3 class="service-name">VOICE</h3>
    </article>
  </section>

  <footer class="footer">
    <div class="brand">
      <span class="brand-dot"></span>
      <div>
        <div class="brand-name">KORVANTIX</div>
        <div class="brand-tagline">BUILT FOR GROWTH</div>
      </div>
    </div>
    <div class="contacts">
      <span class="contact">
        <span class="contact-badge">
          <svg width="22" height="22" viewBox="0 0 24 24"><path fill="#fff" d="M6.6 10.8a15.1 15.1 0 0 0 6.6 6.6l2.2-2.2c.3-.3.7-.4 1-.2 1.1.4 2.3.6 3.6.6.6 0 1 .4 1 1V20c0 .6-.4 1-1 1A17 17 0 0 1 3 4c0-.6.4-1 1-1h3.5c.6 0 1 .4 1 1 0 1.3.2 2.5.6 3.6.1.3 0 .7-.2 1z"/></svg>
        </span>(410)555-0148
      </span>
      <span class="contact-divider"></span>
      <span class="contact">
        <span class="contact-badge">
          <svg width="22" height="22" viewBox="0 0 24 24"><path fill="#fff" d="M3 6h18v12H3z"/><path fill="none" stroke="#1872bb" stroke-width="2" d="M3 6l9 7 9-7"/></svg>
        </span>INFO@KORVANTIX.COM
      </span>
    </div>
    <div class="website">
      <span class="website-badge">
        <svg width="60" height="60" viewBox="0 0 24 24" fill="none" stroke="#fff" stroke-width="1.3"><circle cx="12" cy="12" r="9"/><ellipse cx="12" cy="12" rx="4" ry="9"/><path d="M3 12h18M4.5 7.5h15M4.5 16.5h15"/></svg>
      </span>KORVANTIX.COM
    </div>
  </footer>
</main>
</body>
</html>
```